Individual Needs Design for Marketing Package

****IMPORTANT: Note that I have arranged an agreement with a specific designer to complete the design for the portfolio. Please do not submit any designs***

Goal
I recently resigned from my job in Canada, and I am moving down to Silicon Valley to pursue a career in the technology startup scene - initially doing technical sales. So my goal is to get a sales position with a startup tech company.

In order to land a sales position, I will be going to a startup conference in Silicon Valley which brings together over 2,000 startup technology companies. My goal is to meet the owners of some of these companies and demonstrate that I can be a valuable asset to their company. My challenge is that I have no existing relationships in Silicon Valley and limited experience in sales. So I have put together a portfolio of some of my most significant accomplishments over the past 6 years (see attached file). My hope is that this portfolio will convey that even though I have limited experience, I am passionate, driven, and loyal with a proven track record of achievement. After talking with them for 30 minutes and developing a rapport, I plan on giving this accomplishment portfolio (in addition to my resume) to CEOs of companies for which I could potentially work.

Message to Communicate
After someone reads my portfolio, I want them to view me as passionate, driven, and loyal with a proven track record of achievement. The design can communicate this message in a subtle way. The portfolio should also speak to my professionalism. It should certainly have some personality, but it should err on the side of professionalism.

Competitors
My competitors will be other people at the conference also looking to get sales positions with these startup companies. My main points of differentiation are that I am passionate, driven, and loyal with a proven track record of results. I would like this to be made a feature of the design.

Design Templates
I do not have any specific fonts or colours that I need you to use. The colours scheme and fonts selected should reinforce my key message.

Other Information
I do not own any specialized design software - only the basic microsoft word and powerpoint. However, I will need to be able to add new accomplishments to the portfolio and edit existing ones. Please let me know how this will be possible. I am not sure if it is possible to convert the final file into a file format that I can edit.

Notice that I have arranged the pages into sections. Feel free to rearrange the content within the sections, but please do not change the order of the sections

The size for the marketing package will be regular 8.5 x 11".
Updates

Target Market(s)

The people that will be reading my portfolio are owners of small technology companies in Silicon Valley. They are typically 28-35 years old, and highly logical thinkers. This means that the content is what is ultimately going to sell myself, but the design is what will make them want to read it. Therefore, the content should really stand out over the design.

Industry/Entity Type

Marketing

Requirements
Must have
• ****IMPORTANT: Note that I have arranged an agreement with a specific designer to complete the design for the portfolio. Please do not submit any designs***

I really view this portfolio as my personal marketing package, and that is where I need your expertise. I need you to take the content that I have in my portfolio and turn it into a personal marketing package. I need you to:

1. Design the cover page
2. Design the template for the content pages
3. Format the pictures and text to best fit the design of the pages**

** I would like the final design submission to include the pictures and text included in the attached file all fully formatted. However, when submitting the first iterations, please do not feel obligated to format the entire portfolio because I know that it can be time consuming. Just formatting the title page and the first content page should be enough to give me an idea of what the final portfolio will look like. Once we narrow it down to the final few designs, then we can start formatting the complete portfolio.

```html
<!DOCTYPE html>
<html lang="en">
<head>
<meta charset="utf-8">
<title>Daniel Harper – Portfolio of Accomplishments</title>
<link href="https://fonts.googleapis.com/css2?family=Ubuntu:wght@300;400;500&display=swap" rel="stylesheet">
<style>
  :root {
    --cover-yellow: #f5d505;
    --ink: #3a2a12;
    --rule: #6b5418;
    --tag-light: #9a6844;
    --tag-dark: #6e4424;
    --label-text: #2b1c10;
  }
  html, body {
    margin: 0;
    padding: 0;
    width: 982px;
    height: 1200px;
    overflow: hidden;
    background: var(--cover-yellow);
  }
  .cover {
    position: relative;
    width: 982px;
    height: 1200px;
    background: var(--cover-yellow);
    font-family: "Ubuntu", sans-serif;
    color: var(--ink);
  }
  .name-tag {
    position: absolute;
    left: 50%;
    top: 88px;
    width: 272px;
    height: 182px;
    transform: translateX(-50%);
    background: radial-gradient(ellipse at 50% 40%, var(--tag-light) 0%, var(--tag-dark) 100%);
    border-radius: 0 0 44px 44px;
  }
  .name-tag__text {
    position: absolute;
    left: 0;
    right: 0;
    top: 150px;
    text-align: center;
    color: var(--label-text);
    letter-spacing: 1px;
  }
  .name-tag__first {
    font-size: 40px;
    font-weight: 500;
    line-height: 46px;
  }
  .name-tag__last {
    font-size: 33px;
    font-weight: 300;
    line-height: 40px;
  }
  .rule {
    position: absolute;
    left: 50%;
    height: 1.5px;
    transform: translateX(-50%);
    background: var(--rule);
  }
  .rule--top { top: 303px; width: 250px; }
  .rule--bottom { top: 1146px; width: 290px; }
  .title {
    position: absolute;
    left: 0;
    right: 0;
    top: 322px;
    margin: 0;
    text-align: center;
    font-weight: 300;
    font-size: 52px;
    letter-spacing: 1px;
    line-height: 56px;
  }
  .subtitle {
    position: absolute;
    left: 0;
    right: 0;
    top: 380px;
    margin: 0;
    text-align: center;
    font-weight: 300;
    font-size: 23px;
    line-height: 28px;
    letter-spacing: 1px;
  }
  .website {
    position: absolute;
    left: 0;
    right: 0;
    top: 1102px;
    margin: 0;
    text-align: center;
    font-weight: 300;
    font-size: 31px;
    line-height: 38px;
    letter-spacing: 0.5px;
  }
</style>
</head>
<body>
<main class="cover">
  <div class="name-tag" role="img" aria-label="Stitched leather name tag illustration"></div>
  <div class="name-tag__text">
    <div class="name-tag__first">DANIEL</div>
    <div class="name-tag__last">HARPER</div>
  </div>

  <div class="rule rule--top"></div>
  <h1 class="title">PORTFOLIO</h1>
  <p class="subtitle">OF ACCOMPLISHMENTS</p>

  <p class="website">WWW.DANIELHARPER.COM</p>
  <div class="rule rule--bottom"></div>
</main>
</body>
</html>
```